Shaping Lattice Engineering

We need to design the look and feel for an innovation company with software products for solving complex IT problems following socio-technical theory thinking. The company is heavy in designing of complex systems (like an architect shop). The new design will form the foundation of our brand moving forward. We will approach software projects as if one is building a skyscraper or a bridge. We want to humanize technology and not the other way around. Our target groups will be healthcare and the environment. We will be able to take complex problems and turn them into amazing IT solutions that improve the quality of life for people.

Here are more fragments of ideas that can help:
===============

Motivation

The technology described in the application, coincides with “Steer-Via-Pulse” concept of Lorne Vistrup, which suggests managing a business by managing an informational representation of it : Lorne had the following vision:

"Imagine an enterprise design model that defines the behavior of an entire business. Imagine making this model a part of the corporate informational infrastructure, implementing it on technology that connects all relevant sources and users of information and affords maximum sharing among all parts of the firm. Managers could respond to the read-outs appearing on the console, modifying the flight plan en route based on changes in external conditions, monitoring the performance of delegated responsibilities, sending coordinated directions to subsidiary functions, and experiencing exhilaration upon their execution. It constitutes institutional memory and intelligence, which augment management's ability to run the business”.

This product does what Mr. Vistrup envisioned.

The Objective

QTV offers software products for the specification, construction, assembly, and ongoing management of a digital representation that is an exact mirror image of an enterprise. The main idea is the capability of managing the enterprise by managing an information technology representation of it through software. The idea is to manage the enterprise as a total system involving all aspects of operations. That makes the enterprise and all its information technology representation is inseparable. The implication is that the management of change at the business and IT infrastructure levels are unified. For example, by reconfiguring the information representation of the enterprise one can change business performance. By changing the configuration of the business representation one can actually change the organization’s ability to respond to internal and external events. Management leadership can act with the aid of technology to better respond and improve their ability to guide the organization. The knowledge management feature of the digital representation of the enterprise enables managers to monitor the impact of change and therefore help management assess risk and determine whether mitigating responses are necessary.

The technology and product defines a new approach for the design, implementation, and ongoing execution of software systems that are truly business-like rather than applications and workflows.

Software

```html
<!DOCTYPE html>
<html lang="en">
<head>
<meta charset="utf-8">
<title>Lattice Engineering</title>
<link rel="stylesheet" href="https://fonts.googleapis.com/css2?family=Arimo:ital,wght@0,400;0,700;1,400&family=Playball&display=swap">
<style>
  :root {
    --header-bg: #262626;
    --header-edge: #3a3a3a;
    --brand-cyan: #3cc6e0;
    --search-bg: #454545;
    --nav-text: #c9c9c9;
    --white: #ffffff;
    --pink: #f5245a;
    --yellow: #f1c40f;
    --blue: #3498db;
    --button-text: #111111;
    --footer-bg: #121212;
    --footer-head: #f2f2f2;
    --footer-link: #8a8a8a;
    --ink: #111111;
  }
  * { margin: 0; padding: 0; box-sizing: border-box; }
  html, body { width: 1000px; height: 1200px; overflow: hidden; }
  body { position: relative; font-family: "Arimo", Arial, sans-serif; background: var(--footer-bg); }
  .abs { position: absolute; }

  /* Header */
  .site-header { left: 0; top: 0; width: 1000px; height: 122px; background: var(--header-bg); border-bottom: 6px solid var(--header-edge); }
  .brand { left: 58px; top: 38px; font-size: 21px; color: var(--brand-cyan); letter-spacing: 0.3px; }
  .brand-rule { left: 58px; top: 71px; width: 244px; height: 1px; background: #8a8a8a; }
  .search { left: 650px; top: 46px; width: 249px; height: 25px; background: var(--search-bg); }
  .search svg { position: absolute; right: 8px; top: 2px; }
  .main-nav { left: 0; top: 90px; width: 1000px; font-size: 13px; color: var(--nav-text); }
  .main-nav span { position: absolute; top: 0; }
  .main-nav .current { color: var(--white); }
  .sign-in { color: var(--white); }

  /* Buttons */
  .btn { width: 102px; height: 31px; background: var(--blue); color: var(--button-text); font-weight: 700; font-size: 13px; display: flex; align-items: center; justify-content: center; }

  /* Hero */
  .hero { left: 0; top: 122px; width: 1000px; height: 249px;
    background: radial-gradient(ellipse at 58% 45%, #c9a58d 0%, #a3968e 28%, #8c8c90 55%, #6f7178 100%); }
  .hero-title { left: 84px; top: 163px; font-size: 34px; color: var(--white); letter-spacing: 1px; }
  .hero-text { left: 86px; top: 225px; font-size: 13px; line-height: 15px; color: var(--white); }

  /* Pink feature */
  .feature-new { left: 0; top: 371px; width: 1000px; height: 227px; background: var(--pink); }
  .feature-new h2 { left: 56px; top: 401px; font-size: 30px; line-height: 35px; color: var(--white); font-weight: 700; letter-spacing: 0.5px; }
  .feature-new-text { left: 59px; top: 483px; font-size: 13px; line-height: 15px; color: var(--white); font-weight: 700; }
  .photo-desk { left: 616px; top: 418px; width: 317px; height: 133px;
    background: linear-gradient(110deg, #c7d3de 0%, #8fa1b4 35%, #2b3550 60%, #aebcc8 100%); }

  /* Yellow feature */
  .feature-system { left: 0; top: 598px; width: 1000px; height: 181px; background: var(--yellow); }
  .feature-system h2 { left: 57px; top: 610px; font-size: 30px; line-height: 35px; color: var(--ink); font-weight: 400; letter-spacing: 0.5px; }
  .feature-system-text { left: 57px; top: 678px; font-size: 13px; line-height: 15px; color: var(--ink); font-weight: 700; }
  .photo-monitors { left: 616px; top: 612px; width: 317px; height: 151px;
    background: linear-gradient(100deg, #3a4048 0%, #8a939a 40%, #e4e6e6 70%, #c8c4bd 100%); }

  /* Meeting band */
  .meeting { left: 0; top: 779px; width: 1000px; height: 173px;
    background: linear-gradient(90deg, #3a3633 0%, #5a5552 35%, #4b4845 60%, #2c2a29 100%); }
  .meeting-title { left: 56px; top: 795px; font-family: "Playball", cursive; font-size: 28px; line-height: 34px; color: var(--white); }
  .meeting-title .indent { padding-left: 24px; }
  .meeting-list { left: 101px; top: 870px; font-size: 13px; line-height: 15px; color: var(--white); font-style: italic; list-style: none; }

  .accent-bar { left: 0; top: 952px; width: 1000px; height: 8px; background: var(--blue); }

  /* Footer */
  .site-footer { left: 0; top: 960px; width: 1000px; height: 240px; background: var(--footer-bg); font-style: italic; font-size: 11px; }
  .footer-col { position: absolute; }
  .footer-col h3 { font-size: 11px; font-weight: 400; color: var(--footer-head); }
  .footer-col ul { list-style: none; color: var(--footer-link); }
  .footer-col li { height: 23px; }
  .legal-links { left: 302px; top: 1153px; color: var(--footer-link); font-size: 11px; font-style: italic; }
  .legal-links span { margin-right: 14px; }
  .copyright { left: 0; top: 1180px; width: 1000px; padding-left: 430px; color: var(--footer-link); font-size: 11px; font-style: italic; }
</style>
</head>
<body>

<header class="site-header abs">
  <div class="brand abs">Lattice Engineering</div>
  <div class="brand-rule abs"></div>
  <div class="search abs">
    <svg width="22" height="22" viewBox="0 0 22 22" aria-hidden="true">
      <circle cx="13" cy="9" r="6" fill="none" stroke="#3cc6e0" stroke-width="3"/>
      <line x1="9" y1="13" x2="3" y2="19" stroke="#3cc6e0" stroke-width="3.5" stroke-linecap="round"/>
    </svg>
  </div>
  <nav class="main-nav abs">
    <span class="current" style="left:80px">HOME</span>
    <span style="left:158px">ABOUT</span>
    <span style="left:230px">HOW-TO</span>
    <span style="left:308px">SUPPORT</span>
    <span style="left:392px">CONTACTS</span>
    <span class="sign-in" style="left:842px;top:1px">Sign in</span>
  </nav>
</header>

<section class="hero abs" role="img" aria-label="Photo of a smiling team of colleagues in an office"></section>
<h1 class="hero-title abs" style="font-weight:400">Honestly</h1>
<p class="hero-text abs">I found a Lattice Engineering company<br>See my story and find a device that's perfect for you.</p>
<div class="btn abs" style="left:86px;top:293px">Read more</div>

<section class="feature-new abs"></section>
<div class="feature-new abs" style="background:none;height:0">
  <h2 class="abs" style="position:fixed">Meet the&nbsp; new&nbsp; Lattice<br>Engineering company</h2>
</div>
<p class="feature-new-text abs">See what's new, take a tour, explore new things,<br>and find out the latest tips...</p>
<div class="btn abs" style="left:86px;top:527px">Read more</div>
<div class="photo-desk abs" role="img" aria-label="Photo of an engineer working at two monitors showing charts"></div>

<section class="feature-system abs"></section>
<div class="feature-system abs" style="background:none;height:0">
  <h2 class="abs" style="position:fixed">New system<br>&nbsp;is here</h2>
</div>
<p class="feature-system-text abs">Lorem ipsum dolor sit amet, consectetur adipiscing elit.<br>Fusce lacus leo, mattis quis congue..</p>
<div class="btn abs" style="left:86px;top:732px">Read more</div>
<div class="photo-monitors abs" role="img" aria-label="Photo of a man reviewing work on multiple desktop monitors"></div>

<section class="meeting abs" role="img" aria-label="Photo of a business team meeting around a table with a presentation screen"></section>
<h2 class="meeting-title abs" style="font-weight:400">Smart powe is<br><span class="indent">smart business</span></h2>
<ul class="meeting-list abs">
  <li>Low rates</li>
  <li>energy audits</li>
  <li>power quality analysis</li>
</ul>
<div class="btn abs" style="left:454px;top:894px">Read more</div>

<div class="accent-bar abs"></div>

<footer class="site-footer abs">
  <div class="footer-col" style="left:81px;top:30px">
    <h3>Info for</h3>
    <ul style="margin-top:16px">
      <li>Developers</li><li>IT professionals</li><li>Small business</li><li>Enterprise</li><li>Students</li>
    </ul>
  </div>
  <div class="footer-col" style="left:302px;top:26px">
    <h3>Support</h3>
    <ul style="margin-top:33px">
      <li>Browse support by category</li><li>Browse support by product</li><li>Contact support</li>
    </ul>
  </div>
  <div class="footer-col" style="left:567px;top:26px">
    <h3>Latest info</h3>
    <ul style="margin-top:33px">
      <li>The&nbsp; Lattice engineering Blog</li><li>Lattice engineering&nbsp; newsletter</li><li>Lattice engineering&nbsp;&nbsp; Product Guide</li>
    </ul>
  </div>
  <div class="footer-col" style="left:802px;top:24px">
    <h3>Contact</h3>
    <ul style="margin-top:28px">
      <li>020 7946 0321</li><li>hello@latticeengineering.example</li>
    </ul>
  </div>
</footer>
<div class="legal-links abs">
  <span>Disclaimers</span><span>Terms of Use</span><span>Trademarks</span><span>Privacy &amp; Cookies</span><span>Site Map</span>
</div>
<div class="copyright abs">© 2014 Lattice Engineering</div>

</body>
</html>
```